Bright Harbor Motors Business Card

Would like a cutting edge / high end Automotive Business card design. Please see current card which is old and dated. Would like to maintain the Bright Harbor Motors logo and same information (address, website, etc).

See our website for the look and feel of what we offer - www.brightharbormotors.example

Target Market(s)

Upper class car buyers

Contact Information for Business Card

Modern high end business card design

Requirements
Nice to have
• Carbon Fiber look background

```html
<!DOCTYPE html>
<html lang="en">
<head>
<meta charset="utf-8">
<title>Bright Harbor Motors Business Card</title>
<link href="https://fonts.googleapis.com/css2?family=Roboto:wght@300;400;500;700&display=swap" rel="stylesheet">
<style>
  :root{
    --backdrop:#dfdfdf;
    --card-dark:#050505;
    --card-light:#f1f1f1;
    --ink-light:#ffffff;
    --ink-soft:#d6d6d6;
    --ink-dark:#1e1e1e;
    --ink-mid:#3a3a3a;
    --rule:#9a9a9a;
  }
  *{margin:0;padding:0;box-sizing:border-box}
  html,body{width:1200px;height:800px;overflow:hidden;background:var(--backdrop);font-family:"Roboto",sans-serif}
  .canvas{position:relative;width:1200px;height:800px}

  .card{position:absolute;width:560px;height:320px;border-radius:30px;overflow:hidden}
  .card--front{left:100px;top:80px;background:var(--card-dark);color:var(--ink-light)}
  .card--back{left:540px;top:400px;background:linear-gradient(120deg,#dcdcdc 0%,var(--card-light) 60%,#f7f7f7 100%);color:var(--ink-dark)}

  .car-art{position:absolute}
  .card--front .car-art{left:60px;top:40px;width:460px;height:220px;border-radius:50% 50% 40% 40%;
    background:radial-gradient(ellipse at 50% 55%,rgba(90,90,90,.45) 0%,rgba(40,40,40,.25) 50%,rgba(5,5,5,0) 75%)}
  .card--back .car-art{left:230px;top:20px;width:330px;height:240px;border-radius:45%;
    background:radial-gradient(ellipse at 60% 50%,rgba(160,160,160,.35) 0%,rgba(200,200,200,.15) 50%,rgba(240,240,240,0) 75%)}

  .brand-name{font-weight:500;text-transform:uppercase;letter-spacing:.06em;line-height:1}
  .front-content{position:absolute;inset:0;display:flex;flex-direction:column;align-items:center;justify-content:center;text-align:center}
  .front-content .brand-name{font-size:40px;color:var(--ink-light);border-bottom:1px solid var(--ink-soft);padding-bottom:12px}
  .tagline{margin-top:14px;font-size:13px;font-weight:300;letter-spacing:.04em;color:var(--ink-soft)}
  .values{margin-top:10px;font-size:17px;font-weight:500;letter-spacing:.05em}
  .site{font-size:11px;letter-spacing:.42em;font-weight:300}
  .front-content .site{margin-top:40px;color:var(--ink-soft)}

  .back-brand{position:absolute;right:46px;top:52px;text-align:right}
  .back-brand .brand-name{font-size:22px;color:var(--ink-dark);border-bottom:1px solid var(--ink-dark);padding-bottom:5px}

  .person{position:absolute;left:56px;top:120px}
  .person-name{font-size:26px;font-weight:700;color:var(--ink-dark)}
  .person-role{font-size:16px;font-weight:400;color:var(--ink-mid);margin-top:2px;padding-bottom:8px;border-bottom:1px solid var(--rule);width:190px}
  .contact-list{list-style:none;margin-top:10px}
  .contact-list li{display:flex;align-items:center;gap:10px;font-size:13px;color:var(--ink-mid);height:22px}
  .contact-list svg{width:15px;height:15px;flex:none;fill:none;stroke:var(--ink-dark);stroke-width:1.6}
  .card--back .site{position:absolute;left:0;right:0;bottom:26px;text-align:center;color:var(--ink-mid)}
</style>
</head>
<body>
<main class="canvas">

  <section class="card card--front">
    <div class="car-art" role="img" aria-label="Faint sports car illustration"></div>
    <div class="front-content">
      <div class="brand-name">Bright Harbor Motors</div>
      <p class="tagline">OFFERING THE FINEST IN LUXURY AND EXOTIC SPORTS CARS</p>
      <p class="values">QUALITY | INTEGRITY | SERVICE</p>
      <p class="site">www.brightharbormotors.example</p>
    </div>
  </section>

  <section class="card card--back">
    <div class="car-art" role="img" aria-label="Faint sports car illustration"></div>
    <div class="back-brand"><div class="brand-name">Bright Harbor Motors</div></div>
    <div class="person">
      <h1 class="person-name">Jordan Vale</h1>
      <p class="person-role">Owner</p>
      <ul class="contact-list">
        <li><svg viewBox="0 0 16 16"><path d="M3 2l3 1 1 3-2 1a8 8 0 0 0 4 4l1-2 3 1 1 3-2 1C7 14 2 9 2 4z"/></svg>555.201.4864</li>
        <li><svg viewBox="0 0 16 16"><rect x="2" y="6" width="12" height="8" rx="1"/><path d="M5 6V2h6v4M5 9h1M8 9h1M5 11h1M8 11h1"/></svg>555.201.3520</li>
        <li><svg viewBox="0 0 16 16"><rect x="1.5" y="3.5" width="13" height="9" rx="1"/><path d="M1.5 4l6.5 5 6.5-5"/></svg>jordan@brightharbormotors.example</li>
        <li><svg viewBox="0 0 16 16"><path d="M8 15s5-5 5-9A5 5 0 0 0 3 6c0 4 5 9 5 9z"/><circle cx="8" cy="6" r="1.8"/></svg>180 Harbor Way #A Marina, CA 90000</li>
      </ul>
    </div>
    <p class="site">www.brightharbormotors.example</p>
  </section>

</main>
</body>
</html>
```